International Digitally Led Media Agency Requires a New Website

Brief Outline

• We are a growing business that has been established for approximately 2 years.

• Our current website did the job when Brindle Media began but it has not developed and progressed alongside the business (currently it does not represent nor portray the business appropriately).

• Brindle Media is a digitally led media agency that has numerous arms; 1) production based work (e.g. Paid Advertising, etc.) 2) consultancy and 3) Offline media (such as outdoor, TV, Radio)

• The business is globally focused and the website must reflect this.

• The new website is to portray the business more professionally with thought leadership at the forefront.

• The tone and voice of the website is to be clear, concise and straight talking.

• The website isn't to be a driver of new business (e.g. conversion based for enquiries) but is to support external new business activities. However, the website is to support the thought leadership marketing (specifically around content marketing - webinars, whitepapers, social, etc).

• We must be able to edit/upload/add content to the website very easily.

The current website is www.brindle-media.example

Current clients include
K&T - www.k&t.example
Hollings Marlowe - www.hm.example
QV Heard - www.qvheard.example
Lunglight UK - www.lunglight.example.uk
The Gripwell Academy - www.gripwell-academy.example.uk
Tilo Pensions - www.tilopensions.example
Cobble Loans - www.cobbleloans.example.uk
KRMaltex - www.kr-maltex.example.uk
Wayfarer Lodging Collective - www.wlc.example
Quillmark - www.quillmark.example
Varnish Lane - www.varnishlaneit.example

Reason: We gave some delayed feedback to some desginers looking to enter the project and want to give them a chance to submit their designs.

Target Market(s)

Key decision makers within brands. Marketing Executives/Managers/Directors, Procurement Executives/Managers/Directors, Company Owners, CEO's /MD's

Industry/Entity Type

Business

Coding

Coded - Design and coding required

Number of Pages Required

5+ page

Font styles to use
Sans Serif

Requirements
Must have
• We definitely want video capability and the ability to add pages ourselves.
• We would like the layout to look something like
• HOME
•   
• 7degree3 > CASE STUDIES
• WHAT WE DO > CASE STUDIES
•  
• CONTACT
•  
• CLIENT LOGIN
Nice to have
• Social feeds

```html
<!DOCTYPE html>
<html lang="en">
<head>
<meta charset="utf-8">
<title>Brindle Media</title>
<link href="https://fonts.googleapis.com/css2?family=Open+Sans:wght@400;600;700;800&display=swap" rel="stylesheet">
<style>
:root{
  --gold:#c9962f;
  --gold-dark:#a87a1f;
  --gold-light:#e3bd6a;
  --ink:#2b2b2b;
  --text:#555;
  --muted:#8a8a8a;
  --paper:#ffffff;
  --mist:#eeeeee;
  --line:#d9d9d9;
  --charcoal:#4a4a4a;
}
*{box-sizing:border-box;margin:0;padding:0}
html,body{width:1200px;height:3543px;overflow:hidden}
body{font-family:"Open Sans",Arial,sans-serif;color:var(--text);background:var(--paper);position:relative}
.abs{position:absolute}
a{color:inherit;text-decoration:none}

/* header */
.contact-strip{left:626px;top:12px;width:531px;height:36px;background:var(--gold);clip-path:polygon(22px 0,100% 0,100% 100%,0 100%);display:flex;align-items:center;gap:26px;padding-left:44px;color:#fff;font-size:13px;font-weight:600;white-space:nowrap}
.contact-strip .dot{width:14px;height:14px;border-radius:50%;border:2px solid #fff;display:inline-block;vertical-align:middle;margin-right:6px}
.contact-strip .social{display:flex;gap:5px;margin-left:auto;margin-right:18px}
.contact-strip .social span{width:16px;height:16px;border-radius:50%;border:2px solid #fff}
.brand-disc{left:58px;top:22px;width:156px;height:156px;border-radius:50%;background:var(--paper);box-shadow:0 3px 10px rgba(0,0,0,.18);z-index:3}
.brand-name{left:232px;top:84px;font-size:24px;font-weight:600;color:var(--charcoal);letter-spacing:1px;white-space:nowrap}
.main-nav{left:624px;top:90px;display:flex;gap:18px;font-size:14px;font-weight:700;color:var(--ink);white-space:nowrap}
.main-nav a{padding:6px 8px}
.main-nav a.active{color:var(--gold);border-bottom:3px solid var(--gold)}

/* hero */
.hero-visual{left:12px;top:137px;width:1176px;height:473px;background:radial-gradient(ellipse at 30% 30%,#8fd3f2 0%,#3d9fd1 35%,#1a5c8c 70%,#0e2f4d 100%)}
.hero-band{left:12px;top:610px;width:1176px;height:75px;background:linear-gradient(#111,#2a2a2a);display:flex;align-items:center;justify-content:center;font-size:46px;font-weight:800;color:#fff;letter-spacing:1px}
.hero-band b{color:var(--gold);margin-right:14px}

/* intro */
.intro{left:12px;top:685px;width:1176px;height:165px;background:linear-gradient(#e9e9e9,#d3d3d3)}
.intro p{position:absolute;left:60px;right:60px;top:38px;text-align:center;font-size:17.5px;font-weight:700;color:var(--ink);line-height:27px}
.cta{top:818px;height:50px;width:285px;background:var(--gold);color:#fff;font-size:15px;font-weight:700;display:flex;align-items:center;justify-content:center;padding-left:40px;letter-spacing:.5px;box-shadow:0 4px 6px rgba(0,0,0,.2)}
.cta::before{content:"";position:absolute;left:-4px;top:-6px;width:60px;height:60px;border-radius:50%;background:#fff;border:4px solid var(--gold)}
.cta svg{position:absolute;left:14px;top:7px;z-index:2}

/* section titles */
.section-title{left:0;width:1200px;display:flex;align-items:center;justify-content:center;gap:24px;font-size:24px;font-weight:800;color:var(--gold);white-space:nowrap}
.section-title .rule{width:130px;height:1px;background:var(--line)}
.section-title em{font-style:normal;color:var(--ink)}

/* 7degree3 cards */
.pillars{left:142px;top:1048px;width:914px;height:216px;display:flex;box-shadow:0 6px 10px rgba(0,0,0,.12)}
.pillar{flex:1;border:1px solid var(--gold);border-top:0;padding:74px 28px 0;font-size:13px;line-height:19px;color:var(--text);position:relative}
.pillar.featured{background:var(--gold);color:#fff;margin-top:-34px;padding-top:108px}
.pillar h3{position:absolute;left:132px;top:40px;font-size:16px;font-weight:800;color:var(--ink)}
.pillar.featured h3{top:74px;color:#fff}
.pillar .icon{position:absolute;left:18px;top:-32px;width:104px;height:104px;border-radius:50%;background:var(--gold);border:6px solid #fff;box-shadow:0 2px 6px rgba(0,0,0,.2);display:flex;align-items:center;justify-content:center}
.pillar.featured .icon{top:-30px;background:#fff;border-color:var(--gold)}
.case-btn{left:482px;top:1322px;width:236px;height:38px;background:var(--charcoal);color:#fff;font-size:14px;font-weight:700;display:flex;align-items:center;justify-content:center;border-radius:3px}

/* what we do */
.services-visual{left:12px;top:1412px;width:1176px;height:600px;background:radial-gradient(ellipse at 50% 45%,#f4f4f4 0%,#d8d8d8 60%,#bdbdbd 100%)}
.services-title{top:1474px}
.service-list{font-size:13px;line-height:17px;color:var(--ink);font-weight:600}
.service-list h4{color:var(--gold);font-size:13px;font-weight:800;margin-bottom:2px}
.service-cols{display:grid;grid-template-columns:118px 110px}
.strategy-box{left:111px;top:1705px;width:302px;height:137px;background:rgba(201,150,47,.85);padding:12px 16px;color:#fff}
.strategy-box h4{color:#fff}
.node{width:104px;height:104px;border-radius:50%;background:#fff;border:4px solid #ddd;box-shadow:0 2px 8px rgba(0,0,0,.2);display:flex;align-items:center;justify-content:center;z-index:2}

/* blog */
.blog-title{top:2064px}
.post{top:2142px;width:356px;height:338px;background:#f3f3f3;box-shadow:0 4px 8px rgba(0,0,0,.15)}
.post .photo{height:185px}
.post .date{position:absolute;left:22px;top:132px;width:90px;height:90px;border-radius:50%;background:var(--gold);border:4px solid #fff;color:#fff;text-align:center;font-weight:700;padding-top:12px;line-height:1}
.post .date small{font-size:12px;display:block}
.post .date strong{font-size:30px;display:block;margin:2px 0}
.post .date span{font-size:11px;display:block;border-top:1px solid rgba(255,255,255,.6);margin:0 18px;padding-top:3px}
.post h3{position:absolute;left:16px;top:225px;right:16px;font-size:15px;font-weight:800;color:var(--ink);line-height:19px}
.post p{position:absolute;left:16px;top:266px;right:16px;font-size:12.5px;line-height:17px;color:var(--text)}
.post .more{position:absolute;right:0;bottom:0;width:110px;height:34px;background:var(--gold);color:#fff;font-size:12px;font-weight:700;display:flex;align-items:center;justify-content:center}

/* awards */
.awards-visual{left:12px;top:2532px;width:1176px;height:290px;background:linear-gradient(100deg,#cfcfcf,#f0f0f0 40%,#e2e2e2 70%,#c4c4c4)}
.awards-title{top:2586px}
.badge-a{left:472px;top:2657px;width:90px;height:111px;background:#1f5d9c;border:3px solid #fff;border-radius:6px}
.badge-b{left:619px;top:2660px;width:108px;height:108px;background:#111}

/* feeds */
.feeds-title{top:2880px}
.feed{top:2957px;width:360px;display:flex;gap:14px}
.feed .stamp{width:71px;flex:none;text-align:center;font-weight:800}
.feed .stamp b{display:block;background:#f1f1f1;color:var(--gold);font-size:28px;height:52px;line-height:52px}
.feed .stamp i{display:block;font-style:normal;font-size:10px;color:var(--gold);background:#f1f1f1;margin-top:-14px;padding-bottom:4px}
.feed .stamp span{display:block;background:var(--gold);color:#fff;font-size:14px;height:26px;line-height:26px}
.feed p{font-size:12.5px;line-height:17px;color:var(--text)}
.feed p strong{color:var(--ink);display:block}
.follow{left:507px;top:3087px;width:186px;height:26px;background:#e6e6e6;border:1px solid #cfcfcf;border-radius:3px;font-size:12px;color:var(--charcoal);display:flex;align-items:center;justify-content:center;gap:8px}
.follow i{width:12px;height:12px;border-radius:50%;background:#5aa7d8}

/* footer */
.site-footer{left:12px;top:3208px;width:1176px;height:288px;background:var(--gold);overflow:hidden;color:#fff}
.footer-disc{position:absolute;left:34px;top:0;width:144px;height:144px;border-radius:50%;background:#fff;display:flex;align-items:center;justify-content:center;text-align:center;font-size:16px;font-weight:600;color:var(--charcoal);line-height:20px}
.footer-col{position:absolute;top:52px;font-size:12px;font-weight:700;line-height:19px;white-space:nowrap}
.footer-col h4{font-size:14px;font-weight:800;padding-bottom:8px;margin-bottom:10px;border-bottom:1px solid rgba(255,255,255,.6);width:150px}
.footer-col li{list-style:none}
.footer-col li::before{content:"› "}
.footer-col .row{display:flex;align-items:center;gap:8px;margin-top:14px}
.footer-col .row i{width:20px;height:20px;border-radius:50%;border:2px solid #fff;flex:none}
.legal{left:12px;top:3496px;width:1176px;height:47px;background:#f2f2f2;display:flex;align-items:center;justify-content:space-between;padding:0 24px;font-size:10px;color:var(--muted)}
.legal .social{display:flex;gap:5px}
.legal .social span{width:16px;height:16px;border-radius:50%;border:1.5px solid var(--muted)}
</style>
</head>
<body>

<header>
  <div class="abs contact-strip">
    <span><i class="dot"></i>+44 20 7946 0321</span>
    <span><i class="dot"></i>contact@brindle-media.example</span>
    <span class="social"><span></span><span></span><span></span></span>
  </div>
  <div class="abs brand-disc"></div>
  <div class="abs brand-name">Brindle Media</div>
  <nav class="abs main-nav">
    <a class="active" href="#">HOME</a>
    <a href="#">7DEGREE3</a>
    <a href="#">WHAT WE DO</a>
    <a href="#">CONTACT</a>
    <a href="#">CLIENT LOGIN</a>
  </nav>
</header>

<section class="hero">
  <div class="abs hero-visual" role="img" aria-label="Photograph of a businessman touching a glowing digital interface with floating icons"></div>
  <h1 class="abs hero-band"><b>WE MAKE</b> AMAZING</h1>
</section>

<section class="abs intro">
  <p>Tapping away on our computers in a side street just off Oxford Street in Central London is where you will find us - Brindle Media. We are a digitally led Media agency fuelled by the belief that every client deserves “Amazing” work.</p>
</section>
<a class="abs cta" style="left:300px" href="#">
  <svg width="36" height="36" viewBox="0 0 36 36"><circle cx="18" cy="18" r="11" fill="none" stroke="#c9962f" stroke-width="3"/><path d="M15 12l8 6-8 6z" fill="#c9962f"/></svg>REQUEST A DEMO</a>
<a class="abs cta" style="left:619px" href="#">
  <svg width="36" height="36" viewBox="0 0 36 36"><circle cx="16" cy="16" r="9" fill="none" stroke="#c9962f" stroke-width="3"/><path d="M23 23l7 7" stroke="#c9962f" stroke-width="4"/></svg>DISCOVER MORE</a>

<section class="method">
  <h2 class="abs section-title" style="top:945px"><span class="rule"></span><span>7DEGREE3</span><span class="rule"></span></h2>
  <div class="abs pillars">
    <article class="pillar">
      <div class="icon"><svg width="56" height="56" viewBox="0 0 56 56" fill="none" stroke="#fff" stroke-width="2.5"><circle cx="28" cy="28" r="7"/><circle cx="10" cy="10" r="4"/><circle cx="46" cy="10" r="4"/><circle cx="10" cy="46" r="4"/><circle cx="46" cy="46" r="4"/><path d="M13 13l10 10M43 13L33 23M13 43l10-10M43 43L33 33"/></svg></div>
      <h3>ANALYSE IT</h3>
      Regardless of your current agency situation we will give you an independent view on your strengths and weaknesses in media strategy, resource and execution.
    </article>
    <article class="pillar featured">
      <div class="icon"><svg width="56" height="56" viewBox="0 0 56 56" fill="none" stroke="#444" stroke-width="2.5"><rect x="30" y="6" width="18" height="14"/><rect x="6" y="36" width="18" height="14"/><path d="M39 20v10H15v6M39 30v6"/><circle cx="39" cy="42" r="5"/></svg></div>
      <h3>PLAN IT</h3>
      Focusing on what matters to your business most, we find the right blend of granular, strategic and detailed approaches to help you achieve your goals.
    </article>
    <article class="pillar">
      <div class="icon"><svg width="56" height="56" viewBox="0 0 56 56" fill="none" stroke="#fff" stroke-width="3"><circle cx="26" cy="30" r="18"/><circle cx="26" cy="30" r="10"/><circle cx="26" cy="30" r="3" fill="#fff"/><path d="M26 30L46 10M40 8l6 2 2 6"/></svg></div>
      <h3>SMASH IT</h3>
      The old adage is true - Knowledge is power. Our clients make decisions with confidence because we give them clarity on their media ecosystem.
    </article>
  </div>
  <a class="abs case-btn" href="#">VIEW CASE STUDIES</a>
</section>

<section class="services">
  <div class="abs services-visual" role="img" aria-label="Faded wall of screens showing digital media icons"></div>
  <h2 class="abs section-title services-title"><span>WHAT <em>WE DO</em></span></h2>

  <div class="abs service-list strategy-box">
    <h4>MEDIA STRATEGY</h4>
    Insight<br>Research<br>KPI Setting<br>Forecasting
  </div>

  <svg class="abs" style="left:400px;top:1666px" width="400" height="210" viewBox="0 0 400 210">
    <path d="M16 200A184 184 0 0 1 384 200H306A106 106 0 0 0 94 200Z" fill="#c9962f"/>
    <path d="M36 200A164 164 0 0 1 364 200" fill="none" stroke="#e3bd6a" stroke-width="2"/>
    <line x1="200" y1="16" x2="200" y2="94" stroke="#fff" stroke-width="2"/>
    <line x1="40" y1="110" x2="108" y2="150" stroke="#fff" stroke-width="2"/>
    <line x1="360" y1="110" x2="292" y2="150" stroke="#fff" stroke-width="2"/>
    <text x="200" y="68" fill="#fff" font-family="Open Sans, sans-serif" font-size="24" font-weight="800" text-anchor="middle">02</text>
    <text x="58" y="172" fill="#fff" font-family="Open Sans, sans-serif" font-size="24" font-weight="800">01</text>
    <text x="312" y="172" fill="#fff" font-family="Open Sans, sans-serif" font-size="24" font-weight="800">03</text>
  </svg>
  <div class="abs" style="left:517px;top:1783px;width:166px;height:166px;border-radius:50%;background:#fff;border:6px solid #e6e6e6;box-shadow:0 3px 10px rgba(0,0,0,.25)"></div>

  <div class="abs node" style="left:548px;top:1545px"><svg width="50" height="50" viewBox="0 0 50 50" fill="none" stroke="#c9962f" stroke-width="2.5"><rect x="8" y="6" width="30" height="38"/><path d="M14 16h18M14 24h18M14 32h10"/><rect x="28" y="28" width="14" height="14" fill="#fff"/></svg></div>
  <div class="abs node" style="left:286px;top:1720px"><svg width="50" height="50" viewBox="0 0 50 50" fill="none" stroke="#c9962f" stroke-width="2.5"><path d="M6 6h16v8a4 4 0 1 0 6 0V6h16v16h-8a4 4 0 1 0 0 6h8v16H28v-8a4 4 0 1 0-6 0v8H6V28h8a4 4 0 1 0 0-6H6z"/></svg></div>
  <div class="abs node" style="left:810px;top:1724px"><svg width="50" height="50" viewBox="0 0 50 50" fill="none" stroke="#c9962f" stroke-width="2.5"><path d="M6 40l12-14 10 8 16-20"/><circle cx="6" cy="40" r="3"/><circle cx="18" cy="26" r="3"/><circle cx="28" cy="34" r="3"/><circle cx="44" cy="14" r="3"/></svg></div>

  <div class="abs service-list" style="left:324px;top:1542px">
    <h4>PLANNING &amp; BUYING</h4>
    <div class="service-cols"><span>Programmatic</span><span>Paid Social</span><span>TV</span><span>Paid Search</span><span>Press</span><span>Mobile</span><span>Outdoor</span><span>Digital Impact</span></div>
  </div>
  <div class="abs service-list" style="left:940px;top:1718px">
    <h4>DATA &amp; INSIGHTS</h4>
    Web Analytics<br>Content optimisation<br>A/B Testing<br>Tag Management<br>Live Bespoke Dashboards
  </div>
</section>

<section class="blog">
  <h2 class="abs section-title blog-title"><span class="rule"></span><span>LATEST FROM <em>BLOG</em></span><span class="rule"></span></h2>
  <article class="abs post" style="left:47px">
    <div class="photo" role="img" aria-label="Photograph of a black front door on a London street" style="background:linear-gradient(135deg,#6b5a45,#2e2a26 60%,#8a7b66)"></div>
    <div class="date"><small>SEP</small><strong>12</strong><span>2016</span></div>
    <h3>We do love an industry body</h3>
    <p>We signed up to the Data Marketing Guild this week after a review of the different industry bodies that could be relevant</p>
    <a class="more" href="#">READ MORE ›</a>
  </article>
  <article class="abs post" style="left:422px">
    <div class="photo" role="img" aria-label="Black and white photograph of a busy street with scooters" style="background:linear-gradient(135deg,#9a9a9a,#4a4a4a 55%,#b5b5b5)"></div>
    <div class="date"><small>OCT</small><strong>10</strong><span>2016</span></div>
    <h3>Mara Whitlow report and it is all mobile, mobile, mobile!</h3>
    <p style="top:266px;margin-top:20px">It's out! The 2016 Mara Whitlow report came out this week and it is all mobile, mobile, mobile!</p>
    <a class="more" href="#">READ MORE ›</a>
  </article>
  <article class="abs post" style="left:797px">
    <div class="photo" role="img" aria-label="Photograph of a wooden keyboard on a desk" style="background:linear-gradient(135deg,#e9e2d6,#c9a57a 55%,#f2ece2)"></div>
    <div class="date"><small>OCT</small><strong>05</strong><span>2016</span></div>
    <h3>Copy writing and paid search</h3>
    <p>Will the skills of copy writing finally be valued in paid search ads? Searchly yesterday released this news</p>
    <a class="more" href="#">READ MORE ›</a>
  </article>
</section>

<section class="awards">
  <div class="abs awards-visual" role="img" aria-label="Faded photograph of hands working over papers on a desk"></div>
  <h2 class="abs section-title awards-title"><span>TRADE MEMBER &amp; <em>AWARDS</em></span></h2>
  <div class="abs badge-a" role="img" aria-label="Industry membership badge"></div>
  <div class="abs badge-b" role="img" aria-label="Industry membership badge"></div>
</section>

<section class="feeds">
  <h2 class="abs section-title feeds-title"><span class="rule"></span><span>LATEST <em>FEEDS</em></span><span class="rule"></span></h2>
  <div class="abs feed" style="left:52px">
    <div class="stamp"><b>01</b><i>SEP</i><span>2016</span></div>
    <p><strong>Nam liber tempor cum soluta nobis</strong>Lorem ipsum dolor sit amet, consectetuer adipiscing elit, sed diam nonummy nibh euismod tincidunt ut laoreet dolore magna aliquam erat.</p>
  </div>
  <div class="abs feed" style="left:432px">
    <div class="stamp"><b>24</b><i>AUG</i><span>2016</span></div>
    <p><strong>Nam liber tempor cum soluta nobis</strong>Lorem ipsum dolor sit amet, consectetuer adipiscing elit, sed diam nonummy nibh euismod tincidunt ut laoreet dolore magna aliquam erat.</p>
  </div>
  <div class="abs feed" style="left:812px">
    <div class="stamp"><b>24</b><i>AUG</i><span>2016</span></div>
    <p><strong>Nam liber tempor cum soluta nobis</strong>Lorem ipsum dolor sit amet, consectetuer adipiscing elit, sed diam nonummy nibh euismod tincidunt ut laoreet dolore magna aliquam erat.</p>
  </div>
  <a class="abs follow" href="#"><i></i>Follow @BrindleMedia</a>
</section>

<footer class="abs site-footer">
  <div class="footer-disc">Brindle<br>Media</div>
  <div class="footer-col" style="left:276px">
    <h4>QUICK LINKS</h4>
    <ul><li>HOME</li><li>7DEGREE3</li><li>WHAT WE DO</li><li>CONTACT</li><li>CLIENT LOGIN</li></ul>
  </div>
  <div class="footer-col" style="left:468px">
    <h4>7DEGREE3</h4>
    <ul><li>ANALYSE IT</li><li>PLAN IT</li><li>SMASH IT</li></ul>
  </div>
  <div class="footer-col" style="left:642px">
    <h4>WHAT WE DO</h4>
    <ul><li>MEDIA STRATEGY</li><li>PLANNING &amp; BUYING</li><li>DATA &amp; INSIGHTS</li></ul>
  </div>
  <div class="footer-col" style="left:876px">
    <h4 style="width:200px">CONTACT</h4>
    <div class="row" style="margin-top:0;align-items:flex-start"><i></i><span>BRINDLE MEDIA<br>14 FENWICK ROW<br>LONDON<br>W1X 9QQ</span></div>
    <div class="row"><i></i><span>+44 20 7946 0321</span></div>
    <div class="row"><i></i><span>contact@brindle-media.example</span></div>
  </div>
</footer>
<div class="abs legal">
  <span>COPYRIGHT © 2016 BRINDLE MEDIA. ALL RIGHTS RESERVED.</span>
  <span class="social"><span></span><span></span><span></span></span>
</div>

</body>
</html>
```